MLR showcase

"We're looking for an event poster for a blues music genre "Riverbend Revue" event. Overall feel should be like a vintage concert poster. Consider use of textures / weathering masks, and if photos are (optionally) used, consider posterizing the photos.
Attached is an example concept poster as well as sponsor's logo. All of the text from the concept poster, as well as sponsor's logo, should be used in the new design.
Photos of the three artists involved may *optionally* be used and can be downloaded, if desired, from:
http://marshlanternrecords.com/presskits/mabel/photos/
http://marshlanternrecords.com/presskits/ruth/photos/
http://marshlanternrecords.com/presskits/arnoldpratt/photos/
Final image should be 8.5x11, 300 dpi, but should be legible when reduced to 1/4 of that size for printing 4-up on a 8.5x11 page (or "postcard" size).
Deliverable should include layered Photoshop and/or Illustrator source files, and identification of all fonts used.

```html
<!DOCTYPE html>
<html lang="en">
<head>
<meta charset="utf-8">
<title>Riverbend Revue</title>
<link rel="stylesheet" href="https://fonts.googleapis.com/css2?family=Bebas+Neue&family=Oswald:wght@500;600&family=Staatliches&display=swap">
<style>
  :root {
    --poster-green: #b7c52c;
    --ink: #151510;
    --photo-dark: #2b2d16;
    --photo-mid: #4a4e22;
    --ribbon-red: #c8150f;
    --footer-red: #bf0f0d;
    --paper-white: #f4f2ea;
  }
  html, body { margin: 0; padding: 0; overflow: hidden; background: var(--poster-green); }
  .poster {
    position: relative; width: 927px; height: 1200px; overflow: hidden;
    background: radial-gradient(ellipse at 50% 35%, #c2d034 0%, var(--poster-green) 60%, #a9b626 100%);
  }
  .title {
    position: absolute; left: 0; width: 927px; text-align: center; margin: 0;
    font-family: "Staatliches", sans-serif; color: var(--ink); font-weight: 400; line-height: 1;
  }
  .title-top { top: 40px; font-size: 140px; letter-spacing: 2px; }
  .title-bottom { top: 180px; font-size: 150px; letter-spacing: 1px; }
  .title-flourish {
    position: absolute; top: 235px; width: 84px; height: 44px; background: var(--ink); border-radius: 22px;
  }
  .title-flourish.left { left: 104px; }
  .title-flourish.right { right: 96px; }
  .date-ribbon { position: absolute; left: 127px; top: 336px; width: 630px; height: 64px; }
  .date-ribbon-text {
    position: absolute; left: 0; top: 336px; width: 927px; height: 64px; line-height: 64px; text-align: center; margin: 0;
    font-family: "Oswald", sans-serif; font-weight: 600; font-size: 40px; color: var(--paper-white);
  }
  .venue {
    position: absolute; left: 0; top: 410px; width: 927px; text-align: center; margin: 0;
    font-family: "Oswald", sans-serif; font-weight: 600; font-size: 44px; color: var(--ink); letter-spacing: 1px;
  }
  .artist-photo {
    position: absolute; background: linear-gradient(180deg, var(--photo-mid) 0%, var(--photo-dark) 45%, #1d1e0e 100%);
    border-radius: 140px 140px 0 0;
  }
  .photo-mabel { left: 70px; top: 560px; width: 300px; height: 467px; }
  .photo-ruth { left: 592px; top: 600px; width: 300px; height: 427px; }
  .photo-arnold { left: 360px; top: 512px; width: 280px; height: 515px; }
  .set-time { position: absolute; }
  .set-time svg { position: absolute; left: 0; top: 0; }
  .set-time span {
    position: absolute; top: 0; width: 100%; text-align: center; line-height: 50px;
    font-family: "Oswald", sans-serif; font-weight: 600; color: var(--paper-white); font-size: 36px;
  }
  .time-mabel { left: 48px; top: 550px; width: 124px; height: 50px; }
  .time-arnold { left: 542px; top: 533px; width: 134px; height: 50px; }
  .time-ruth { left: 784px; top: 618px; width: 116px; height: 50px; }
  .artist {
    position: absolute; text-align: center; color: var(--paper-white);
    text-shadow: 0 2px 6px rgba(0,0,0,.7);
  }
  .artist-name {
    margin: 0; font-family: "Bebas Neue", sans-serif; font-weight: 400; font-size: 80px; line-height: .9; letter-spacing: 1px;
  }
  .artist-tag {
    margin: 16px 0 0; font-family: "Oswald", sans-serif; font-weight: 500; font-size: 20px; line-height: 1.25;
  }
  .artist-mabel { left: 90px; top: 752px; width: 270px; }
  .artist-arnold { left: 370px; top: 752px; width: 230px; }
  .artist-ruth { left: 626px; top: 790px; width: 230px; }
  .footer {
    position: absolute; left: 0; top: 1027px; width: 927px; height: 173px; background: var(--footer-red);
    font-family: "Oswald", sans-serif; font-weight: 600; color: var(--paper-white);
  }
  .presented-by { position: absolute; left: 143px; top: 68px; font-size: 22px; letter-spacing: .5px; }
  .sponsor-name {
    position: absolute; left: 330px; top: 52px; width: 270px; text-align: center;
    font-size: 30px; line-height: 1.05; letter-spacing: 1px;
  }
  .sponsor-url { position: absolute; left: 620px; top: 68px; font-size: 22px; }
</style>
</head>
<body>
<main class="poster">
  <h1 class="title title-top">River★bend</h1>
  <div class="title-flourish left" role="img" aria-label="Decorative scroll ornament"></div>
  <p class="title title-bottom">Revue</p>
  <div class="title-flourish right" role="img" aria-label="Decorative scroll ornament"></div>

  <svg class="date-ribbon" viewBox="0 0 630 64" aria-hidden="true">
    <polygon points="0,0 630,0 608,32 630,64 0,64 22,32" fill="var(--ink)"/>
  </svg>
  <p class="date-ribbon-text">Thu May 9 • ADM: FREE</p>
  <p class="venue">@ DELTA JACK'S • 218 LEVEE</p>

  <div class="artist-photo photo-mabel" role="img" aria-label="Posterized photo of Mabel Tate holding a bass guitar"></div>
  <div class="artist-photo photo-ruth" role="img" aria-label="Posterized photo of Ruth Crane smiling"></div>
  <div class="artist-photo photo-arnold" role="img" aria-label="Posterized photo of Arnold Pratt in a wide-brimmed hat"></div>

  <div class="set-time time-mabel">
    <svg width="124" height="50" viewBox="0 0 124 50" aria-hidden="true"><polygon points="0,0 124,0 124,50 0,50 16,25" fill="var(--ribbon-red)"/></svg>
    <span>12:45</span>
  </div>
  <div class="set-time time-arnold">
    <svg width="134" height="50" viewBox="0 0 134 50" aria-hidden="true"><polygon points="0,0 134,0 114,25 134,50 0,50" fill="var(--ribbon-red)"/></svg>
    <span style="width:114px">1:45</span>
  </div>
  <div class="set-time time-ruth">
    <svg width="116" height="50" viewBox="0 0 116 50" aria-hidden="true"><polygon points="0,0 116,0 98,25 116,50 0,50" fill="var(--ribbon-red)"/></svg>
    <span style="width:98px">2:45</span>
  </div>

  <section class="artist artist-mabel">
    <h2 class="artist-name">Mabel<br>Tate</h2>
    <p class="artist-tag">INTELLIGENTLY SEXY<br>SLYLY SUBVERSIVE</p>
  </section>
  <section class="artist artist-arnold">
    <h2 class="artist-name">Arnold<br>Pratt</h2>
    <p class="artist-tag">AS SEEN ON<br>“BACKROADS”</p>
  </section>
  <section class="artist artist-ruth">
    <h2 class="artist-name">Ruth<br>Crane</h2>
    <p class="artist-tag">“BAYOU<br>SPITFIRE”</p>
  </section>

  <footer class="footer">
    <span class="presented-by">PRESENTED BY</span>
    <span class="sponsor-name">MARSH LANTERN<br>RECORDS</span>
    <span class="sponsor-url">MARSHLANTERNRECORDS.COM</span>
  </footer>
</main>
</body>
</html>
```